School Signage

I am wanting designs for signs completed that prompt students of the school requirements for hats, preparation and play.

I've uploaded rough examples of what we're after, but we would like them stylised and better than the example, including:
- A stylised logo/graphic for the 'Wallumba 1, 2, 3'
- Clear, crisp signage for the words.
- Graphics that reinforce the message of the sign.

We're after three signs:
- One that will be located on the oval to prompt hat use.
- One that will be near the entry prompting the morning routine (please make this one landscape with instructions for 'on time' on one side, and 'late' on the other).
- One that will be located within the school prompting readiness for class.

```html
<!DOCTYPE html>
<html lang="en">
<head>
<meta charset="utf-8">
<title>Ready for Class Sign</title>
<link rel="stylesheet" href="https://fonts.googleapis.com/css2?family=Arimo:wght@400;700&display=swap">
<style>
  :root {
    --sign-yellow: #f9e814;
    --school-green: #1b3d21;
    --ink-green: #1e3f22;
    --pattern-green: #2a5231;
    --value-yellow: #f9e814;
    --white: #ffffff;
    --backdrop: #ececec;
  }
  html, body {
    margin: 0;
    padding: 0;
    width: 1200px;
    height: 1200px;
    overflow: hidden;
    background: var(--backdrop);
    font-family: "Arimo", Arial, sans-serif;
  }
  .canvas {
    position: relative;
    width: 1200px;
    height: 1200px;
  }
  .sign {
    position: absolute;
    left: 80px;
    top: 275px;
    width: 1040px;
    height: 650px;
    background: var(--sign-yellow);
    overflow: hidden;
  }
  .sign-shapes {
    position: absolute;
    inset: 0;
  }
  .school-name {
    position: absolute;
    left: 52px;
    top: 70px;
    width: 176px;
    display: flex;
    flex-direction: column;
    align-items: center;
    gap: 12px;
    text-align: center;
    color: var(--ink-green);
    font-weight: 700;
    font-size: 22px;
    line-height: 1.15;
  }
  .school-name .mark {
    width: 54px;
    height: 54px;
    border-radius: 50%;
    background: var(--school-green);
  }
  .headline {
    position: absolute;
    left: 264px;
    top: 46px;
    margin: 0;
    color: var(--ink-green);
    font-weight: 700;
    font-size: 56px;
    line-height: 1;
    letter-spacing: 0.2px;
  }
  .subhead {
    position: absolute;
    left: 264px;
    top: 128px;
    margin: 0;
    color: var(--ink-green);
    font-weight: 700;
    font-size: 42px;
    line-height: 1;
  }
  .checklist {
    list-style: none;
    margin: 0;
    padding: 0;
  }
  .check-item {
    position: absolute;
    display: flex;
    align-items: flex-start;
    gap: 14px;
    color: var(--ink-green);
    font-weight: 700;
    font-size: 29px;
    line-height: 40px;
  }
  .check-item .icon {
    flex: none;
    width: 46px;
    height: 46px;
    margin-top: -3px;
  }
  .item-laptop { left: 167px; top: 248px; }
  .item-phone { left: 603px; top: 248px; }
  .item-uniform { left: 603px; top: 348px; }
  .values {
    position: absolute;
    left: 354px;
    top: 468px;
    width: 306px;
    text-align: right;
  }
  .values-title {
    margin: 0;
    color: var(--white);
    font-weight: 700;
    font-size: 28px;
    line-height: 1.1;
    text-align: left;
  }
  .values-label {
    margin: 2px 0 0;
    color: var(--value-yellow);
    font-weight: 700;
    font-size: 17px;
    line-height: 1.2;
  }
</style>
</head>
<body>
<div class="canvas">
  <section class="sign">
    <svg class="sign-shapes" viewBox="0 0 1040 650" width="1040" height="650" aria-hidden="true">
      <defs>
        <linearGradient id="patternTone" x1="0" y1="0" x2="0" y2="1">
          <stop offset="0" stop-color="#1b3d21"/>
          <stop offset="1" stop-color="#2a5231"/>
        </linearGradient>
      </defs>
      <path class="green-wave" fill="#1b3d21"
        d="M0 420 C120 385 230 378 360 392 C520 410 640 450 800 462 C900 469 980 464 1040 460 L1040 650 L0 650 Z"/>
    </svg>
    <svg class="sign-shapes" viewBox="0 0 1040 650" width="1040" height="650" role="img" aria-label="Decorative dotted and flowing line pattern across the green band">
      <path fill="url(#patternTone)" opacity="0.9"
        d="M0 545 C200 520 400 600 600 610 C760 618 900 560 1040 520 L1040 650 L0 650 Z"/>
    </svg>

    <div class="school-name">
      <span class="mark"></span>
      <span>Wallumba State High</span>
    </div>

    <h1 class="headline">Are you ready for class?</h1>
    <h2 class="subhead">The Wallumba 1, 2, 3</h2>

    <ul class="checklist">
      <li class="check-item item-laptop">
        <svg class="icon" viewBox="0 0 46 46" aria-hidden="true">
          <circle cx="23" cy="23" r="21.5" fill="none" stroke="#1e3f22" stroke-width="2"/>
          <rect x="13" y="14" width="20" height="13" rx="1" fill="none" stroke="#1e3f22" stroke-width="2"/>
          <path d="M10 30 H36 L34 33 H12 Z" fill="#1e3f22"/>
        </svg>
        <span>1. Laptop/workbook</span>
      </li>
      <li class="check-item item-phone">
        <svg class="icon" viewBox="0 0 46 46" aria-hidden="true">
          <circle cx="23" cy="23" r="21.5" fill="none" stroke="#1e3f22" stroke-width="2"/>
          <rect x="15" y="11" width="14" height="24" rx="2.5" fill="#8a8a8a" stroke="#1e3f22" stroke-width="1.5"/>
          <rect x="13" y="22" width="20" height="14" rx="3" fill="#5e5e5e"/>
          <circle cx="22" cy="32.5" r="1" fill="#d9d9d9"/>
        </svg>
        <span>2. Phone in Pocketlock</span>
      </li>
      <li class="check-item item-uniform">
        <svg class="icon" viewBox="0 0 46 46" aria-hidden="true">
          <circle cx="23" cy="23" r="21.5" fill="none" stroke="#1e3f22" stroke-width="2"/>
          <path d="M12 27 C12 18 17 14 23 14 C29 14 33 18 33 26 Z" fill="none" stroke="#1e3f22" stroke-width="2" stroke-linejoin="round"/>
          <path d="M12 27 C18 29 26 30 36 29" fill="none" stroke="#1e3f22" stroke-width="2" stroke-linecap="round"/>
          <path d="M23 14 V26" stroke="#1e3f22" stroke-width="1.5"/>
        </svg>
        <span>3. Correct uniform<br>(including hat)</span>
      </li>
    </ul>

    <div class="values">
      <p class="values-title">Curiosity and Drive</p>
      <p class="values-label">Wallumba Learner Values</p>
    </div>
  </section>
</div>
</body>
</html>
```